Web site for Tree Removal Company

What we are looking for:
-------------------------------
Looking for a wordpress web site, you can provide your own template or we can supply you with one (http://quorvel.plindatheme.net).

What we do
---------------
To see what we do please go to google Australia and google "Tree removal Sydney" or "Tree Removal Melbourne".

Web site requirements
-----------------------------
We prefer you to use our template as it has all our requirements in already.
- Responsive.
- Based on Wordpress.
- Full complaint and compatible with plugs.

Look, Feel and Appearance
------------------------------------
Please use the logo (see attached), for colour scheme, look and feel of the web site.

Thank you for your time and effort!

Target Market(s)

Tree Removal for Residential Homes

Industry/Entity Type

It Company

Number of Pages Required

4 page

Font styles to use
Serif
Sans Serif

Requirements
Must have
• Wordpress
Nice to have
• Original artwork, images and text
Should not have
• non related images or wording

```html
<!DOCTYPE html>
<html lang="en">
<head>
<meta charset="utf-8">
<title>Leafwell — Tree Services</title>
<link href="https://fonts.googleapis.com/css2?family=Quicksand:wght@500;700&family=Open+Sans:wght@400;600;700&display=swap" rel="stylesheet">
<style>
:root{
  --orange:#f7a21b;
  --dark:#2b2b2b;
  --footer:#2d2d2d;
  --grey-bg:#ededed;
  --text:#666;
  --heading:#333;
  --white:#fff;
}
*{box-sizing:border-box;margin:0;padding:0}
html,body{width:1200px;height:2752px;overflow:hidden}
body{font-family:"Open Sans",Arial,sans-serif;color:var(--text);background:var(--white);position:relative}
.section{position:absolute;left:0;width:1200px}
.heading{font-family:"Quicksand",Arial,sans-serif;font-weight:700;color:var(--heading);font-size:40px;letter-spacing:2px;text-align:center}
.lead{font-size:15px;line-height:26px;text-align:center;color:var(--text)}
.btn{display:inline-block;background:var(--orange);color:var(--white);font-size:15px;font-weight:600;padding:9px 22px;border-radius:3px}
.brand-dot{display:block;border-radius:50%;background:var(--white)}

/* hero */
.hero{top:0;height:660px;background:linear-gradient(180deg,#2e3a2c 0%,#4c5b3a 45%,#3d4630 75%,#25291f 100%)}
.hero-photo{position:absolute;inset:0;background:radial-gradient(ellipse at 50% 70%,rgba(150,160,110,.45),rgba(0,0,0,0) 60%)}
.brand{position:absolute;left:72px;top:14px;display:flex;align-items:center;gap:10px;color:var(--white);font-family:"Quicksand",sans-serif;font-weight:700;font-size:18px;letter-spacing:1px}
.brand .brand-dot{width:40px;height:40px;opacity:.85}
.nav{position:absolute;right:72px;top:0;display:flex;gap:44px}
.nav a{color:var(--white);text-decoration:none;font-size:15px;padding-top:44px;display:block}
.nav a.active{color:var(--orange);border-top:4px solid var(--orange);padding-top:40px}
.hero-title{position:absolute;top:186px;width:100%;text-align:center;color:var(--white);font-family:"Quicksand",sans-serif;font-weight:700;font-size:42px;letter-spacing:3px}
.service-strip{position:absolute;left:250px;top:268px}
.hero-text{position:absolute;top:460px;left:380px;width:440px;color:var(--white);font-size:15px;line-height:24px;text-align:center}
.hero-cta{position:absolute;top:530px;width:100%;text-align:center}

/* welcome */
.welcome{top:660px;height:320px}
.welcome .heading{margin-top:58px}
.welcome .lead{width:1000px;margin:34px auto 0}
.welcome .cta{text-align:center;margin-top:30px}
.welcome .btn{padding:8px 20px;font-size:14px}

/* offer */
.offer{top:980px;height:720px;background:var(--grey-bg)}
.offer .heading{margin-top:32px}
.offer .lead{width:1000px;margin:22px auto 0}
.wheel{position:absolute;left:440px;top:240px}
.offer-item{position:absolute;width:200px;font-size:13px;line-height:19px}
.offer-item h3{font-family:"Quicksand",sans-serif;font-size:19px;font-weight:700;color:var(--heading);margin-bottom:4px}
.offer-item.left{text-align:right}
.offer-item.highlight h3{color:var(--orange)}

/* special */
.special{top:1700px;height:340px}
.special .heading{margin-top:84px}
.special .lead{width:1000px;margin:26px auto 0}
.special .cta{text-align:center;margin-top:26px}

/* testimonials */
.testimonials{top:2040px;height:372px;background:var(--grey-bg)}
.testimonials .heading{margin-top:60px}
.testimonial{position:absolute;top:160px;width:330px;display:flex;gap:18px}
.avatar{flex:none;width:112px;height:112px;border-radius:50%;background:linear-gradient(160deg,#bdbdbd,#6d6d6d)}
.testimonial h4{font-size:14px;font-weight:700;color:var(--heading);margin-top:10px}
.testimonial p{font-size:13px;line-height:19px;margin-top:4px}

/* footer */
.footer{top:2412px;height:340px;background:var(--footer);color:#ccc}
.footer-brand{position:absolute;left:130px;top:56px;width:120px;text-align:center}
.footer-brand .brand-dot{width:70px;height:70px;margin:0 auto 10px}
.footer-brand span{font-family:"Quicksand",sans-serif;font-weight:700;color:var(--white);font-size:18px;letter-spacing:1px}
.socials{position:absolute;left:134px;top:196px;display:flex;gap:14px}
.socials i{width:28px;height:28px;border-radius:50%;background:#555;display:block}
.copyright{position:absolute;left:130px;top:246px;font-size:13px;color:#ddd}
.footer-col{position:absolute;top:86px}
.footer-col h5{color:var(--orange);font-size:18px;font-weight:400;margin-bottom:12px}
.footer-col li{list-style:none;font-size:15px;line-height:32px;color:#ddd}
.footer-col li::before{content:"•";margin-right:10px}
.footer-col li.active{color:var(--orange)}
.contact-row{display:flex;align-items:center;gap:10px;font-size:15px;line-height:36px;color:#ddd}
.contact-row b{color:var(--white);font-weight:700}
</style>
</head>
<body>

<header class="section hero">
  <div class="hero-photo" role="img" aria-label="Photograph of a shaded tree-lined avenue"></div>
  <div class="brand"><i class="brand-dot"></i>Leafwell</div>
  <nav class="nav">
    <a class="active">Home</a><a>About Us</a><a>Services</a><a>Contact Us</a>
  </nav>
  <h1 class="hero-title">Any Tree Any Place</h1>
  <svg class="service-strip" width="700" height="132" viewBox="0 0 700 132" font-family="Open Sans, sans-serif" font-size="14" font-weight="700" fill="#222">
    <g fill="#fff" stroke="#222" stroke-width="2">
      <polygon points="0,130 100,2 200,130"/>
      <polygon points="100,2 300,2 200,130"/>
      <polygon points="200,130 300,2 400,130"/>
      <polygon points="300,2 500,2 400,130"/>
      <polygon points="400,130 500,2 600,130"/>
      <polygon points="500,2 700,2 600,130"/>
    </g>
    <text x="100" y="118" text-anchor="middle">Tree Removal</text>
    <text x="200" y="24" text-anchor="middle">Stump Grinding</text>
    <text x="300" y="118" text-anchor="middle">Tree Pruning</text>
    <text x="400" y="24" text-anchor="middle">Arborist</text>
    <text x="500" y="118" text-anchor="middle">Tree Planting</text>
    <text x="600" y="24" text-anchor="middle">Hedge Trimming</text>
  </svg>
  <p class="hero-text">Careful tree work done safely, cleanly and on time. Local crews who look after your yard like their own.</p>
  <div class="hero-cta"><span class="btn">Free Online Quote</span></div>
</header>

<section class="section welcome">
  <h2 class="heading">Welcome to Leafwell</h2>
  <p class="lead">We are a local team caring for trees around family homes. From a single branch to a full removal, our trained crews plan each job with care, protect your garden and leave the site tidy. Honest advice, fair quotes and friendly service every time you call us.</p>
  <div class="cta"><span class="btn">more</span></div>
</section>

<section class="section offer">
  <h2 class="heading">What we offer</h2>
  <p class="lead">A full range of tree services for residential homes, delivered by insured and experienced arborists. Here is how we can help you keep your trees healthy and your home safe.</p>

  <svg class="wheel" width="320" height="320" viewBox="0 0 320 320">
    <circle cx="160" cy="160" r="152" fill="none" stroke="#f7a21b" stroke-width="3"/>
    <circle cx="160" cy="160" r="136" fill="#7a6a45"/>
    <circle cx="10" cy="100" r="9" fill="#f7a21b"/>
    <circle cx="18" cy="222" r="7" fill="#444"/>
    <circle cx="88" cy="295" r="7" fill="#444"/>
    <circle cx="305" cy="100" r="7" fill="#444"/>
    <circle cx="300" cy="222" r="7" fill="#444"/>
    <circle cx="232" cy="295" r="7" fill="#444"/>
  </svg>
  <div role="img" aria-label="Photograph of hands holding a young seedling" style="position:absolute;left:464px;top:264px;width:272px;height:272px;border-radius:50%;background:radial-gradient(circle at 50% 45%,#8fae52,#6b5b3c 70%)"></div>

  <div class="offer-item left highlight" style="left:240px;top:240px"><h3>Tree Planting</h3>New trees chosen and placed to thrive for years.</div>
  <div class="offer-item left" style="left:240px;top:380px"><h3>Tree Pruning</h3>Shaping cuts that keep trees strong and safe.</div>
  <div class="offer-item left" style="left:240px;top:530px"><h3>Tree Planting</h3>Healthy stock planted with care and good soil.</div>
  <div class="offer-item" style="left:770px;top:240px"><h3>Stump Grinding</h3>Stumps ground below ground level, site cleared.</div>
  <div class="offer-item" style="left:790px;top:380px"><h3>Arborist</h3>Expert checks on tree health and risk.</div>
  <div class="offer-item" style="left:770px;top:530px"><h3>Hedge Trimming</h3>Neat even hedges for a tidy front yard.</div>
</section>

<section class="section special">
  <h2 class="heading">Monthly Special</h2>
  <p class="lead">Book any pruning job this month and get stump grinding at half price. Ask our team for details when you call for a quote.</p>
  <div class="cta"><span class="btn">Join now</span></div>
</section>

<section class="section testimonials">
  <h2 class="heading">Testimonials</h2>
  <div class="testimonial" style="left:80px">
    <div class="avatar" role="img" aria-label="Portrait photo of a customer"></div>
    <div><h4>RHYS CALDER</h4><p>Fast, friendly crew. The old gum is gone and the yard looks great.</p></div>
  </div>
  <div class="testimonial" style="left:460px">
    <div class="avatar" role="img" aria-label="Portrait photo of a customer"></div>
    <div><h4>NINA HOLLOWAY</h4><p>Clear quote, on time and they cleaned up every leaf.</p></div>
  </div>
  <div class="testimonial" style="left:860px">
    <div class="avatar" role="img" aria-label="Portrait photo of a customer"></div>
    <div><h4>OWEN MARSH</h4><p>Great advice on our hedges. Would happily call them again.</p></div>
  </div>
</section>

<footer class="section footer">
  <div class="footer-brand"><i class="brand-dot"></i><span>LEAFWELL</span></div>
  <div class="socials"><i></i><i></i><i></i></div>
  <p class="copyright">Copyright © Leafwell</p>

  <div class="footer-col" style="left:480px">
    <h5>Navigation links</h5>
    <ul>
      <li class="active">Home</li><li>About Us</li><li>Services</li><li>Contact Us</li>
    </ul>
  </div>

  <div class="footer-col" style="left:780px">
    <h5>Location</h5>
    <div class="contact-row">
      <svg width="16" height="16" viewBox="0 0 16 16"><path d="M8 1a5 5 0 0 0-5 5c0 4 5 9 5 9s5-5 5-9a5 5 0 0 0-5-5zm0 7a2 2 0 1 1 0-4 2 2 0 0 1 0 4z" fill="#ddd"/></svg>
      <span><b>Address:</b> 48 Fernbrook Lane, Eastvale</span>
    </div>
    <div class="contact-row">
      <svg width="16" height="16" viewBox="0 0 16 16"><path d="M3 1h3l1 4-2 1a9 9 0 0 0 5 5l1-2 4 1v3a2 2 0 0 1-2 2A13 13 0 0 1 1 3a2 2 0 0 1 2-2z" fill="#ddd"/></svg>
      <span><b>Phone:</b> (020) 555-0148</span>
    </div>
    <div class="contact-row">
      <svg width="16" height="16" viewBox="0 0 16 16"><rect x="1" y="3" width="14" height="10" rx="1" fill="#ddd"/><path d="M1 4l7 5 7-5" stroke="#2d2d2d" stroke-width="1.5" fill="none"/></svg>
      <span><b>Email:</b> hello@leafwell.test</span>
    </div>
  </div>
</footer>

</body>
</html>
```